The Willow Hearth: Steady Horizon

Please use the attached images as a reference and as inspiration for this contest. Please note, these images are google searched and belong to someone else.
This project is for our church.
We have a new Sermon Series launching and we want to be able to promote it and manipulate the size of the project via Facebook Cover Art, CD Labels, T-Shirts, Banners, etc.
Requesting a HD 1080 X 920 pixels.
Need an editable PSD file from the winner of the contest.
The title of the project is: Steady Horizon.
The idea behind this project is bringing things in life into focus to help our congregation be intentional about focusing on making positive changes to major areas of life.
When we think of this - we think of a camera brining something into focus to take that perfect shot, or as one of the attached images show blurry images coming into focus.
Keywords that can be used in the design are: Faith, Family, Finances, and Fitness.
Just because it is for a church does NOT mean we need it to look like its for a church. In fact, we desire the design to be compelling to someone who has never stepped foot into a church building. Avoid a "church" look.
Good Luck!
Target Market(s)
Everyone
Industry/Entity Type
House
Requirements
Must have
- Bringing "things" into focus.
- Please read description for more details
Should not have
- A church look

```html
<!DOCTYPE html>
<html lang="en">
<head>
<meta charset="utf-8">
<title>Steady Horizon — Sermon Series</title>
<link rel="stylesheet" href="https://fonts.googleapis.com/css2?family=Fredoka:wght@600;700&display=swap">
<style>
  :root {
    --sky: #6fb0d8;
    --sky-deep: #3f86b8;
    --dusk: #2a2f44;
    --amber: #f2b233;
    --ember: #e8563a;
    --rose: #f0a38f;
    --peach: #f7c49a;
    --ink-white: #ffffff;
  }
  * { margin: 0; padding: 0; box-sizing: border-box; }
  html, body {
    width: 1200px;
    height: 1022px;
    overflow: hidden;
    background: #ffffff;
  }
  .cover {
    position: relative;
    width: 1200px;
    height: 1022px;
    overflow: hidden;
    font-family: "Fredoka", "Arial Rounded MT Bold", sans-serif;
    color: var(--ink-white);
  }
  .cover__backdrop {
    position: absolute;
    inset: 0;
    background:
      radial-gradient(ellipse 260px 160px at 300px 420px, rgba(20,20,30,0.75), transparent 70%),
      radial-gradient(ellipse 200px 120px at 880px 200px, rgba(20,20,30,0.6), transparent 70%),
      radial-gradient(ellipse 180px 90px at 560px 300px, rgba(242,178,51,0.85), transparent 70%),
      radial-gradient(ellipse 140px 80px at 300px 180px, rgba(242,178,51,0.7), transparent 70%),
      radial-gradient(ellipse 160px 90px at 1080px 390px, rgba(242,200,60,0.8), transparent 70%),
      radial-gradient(ellipse 120px 90px at 760px 420px, rgba(232,60,70,0.75), transparent 70%),
      radial-gradient(ellipse 90px 70px at 1010px 220px, rgba(230,70,130,0.6), transparent 70%),
      radial-gradient(ellipse 90px 50px at 290px 450px, rgba(255,240,230,0.7), transparent 70%),
      radial-gradient(ellipse 240px 120px at 200px 740px, rgba(247,210,110,0.8), transparent 70%),
      radial-gradient(ellipse 300px 200px at 1000px 800px, rgba(240,163,143,0.8), transparent 70%),
      radial-gradient(ellipse 260px 160px at 560px 700px, rgba(120,140,190,0.55), transparent 70%),
      linear-gradient(180deg, var(--sky) 0%, var(--sky-deep) 22%, var(--dusk) 42%, var(--ember) 56%, var(--peach) 72%, var(--rose) 100%);
  }
  .cover__title {
    position: absolute;
    left: 0;
    right: 0;
    text-align: center;
    text-transform: uppercase;
    line-height: 1;
  }
  .cover__kicker {
    top: 70px;
    font-weight: 700;
    font-size: 46px;
    letter-spacing: 3px;
  }
  .cover__headline {
    top: 118px;
    font-weight: 700;
    font-size: 178px;
    letter-spacing: 2px;
  }
  .cover__viewfinder {
    position: absolute;
    inset: 0;
    width: 1200px;
    height: 1022px;
  }
  .viewfinder__stroke {
    fill: none;
    stroke: var(--ink-white);
    stroke-width: 2.5;
    stroke-linecap: round;
  }
  .viewfinder__bracket { stroke-width: 4; stroke-linecap: butt; }
  .cover__label {
    position: absolute;
    left: 0;
    right: 0;
    top: 950px;
    text-align: center;
    font-weight: 700;
    font-size: 30px;
    letter-spacing: 2px;
    text-transform: uppercase;
  }
</style>
</head>
<body>
  <main class="cover">
    <div class="cover__backdrop" role="img" aria-label="Blurred night city street with glowing warm lights under a blue evening sky"></div>

    <h1 class="cover__title">
      <span class="cover__title cover__kicker">Steady</span>
      <span class="cover__title cover__headline">Horizon</span>
    </h1>

    <svg class="cover__viewfinder" viewBox="0 0 1080 920" preserveAspectRatio="none" aria-hidden="true">
      <g class="viewfinder__stroke">
        <path d="M370 335 A211 211 0 0 1 415 290"/>
        <path d="M665 290 A211 211 0 0 1 710 335"/>
        <path d="M710 585 A211 211 0 0 1 665 630"/>
        <path d="M415 630 A211 211 0 0 1 370 585"/>
      </g>
      <g class="viewfinder__stroke">
        <rect x="532" y="294" width="16" height="16"/>
        <rect x="322" y="350" width="16" height="16"/>
        <rect x="742" y="350" width="16" height="16"/>
        <rect x="202" y="452" width="16" height="16"/>
        <rect x="322" y="452" width="16" height="16"/>
        <rect x="532" y="452" width="16" height="16"/>
        <rect x="742" y="452" width="16" height="16"/>
        <rect x="862" y="452" width="16" height="16"/>
        <rect x="322" y="554" width="16" height="16"/>
        <rect x="742" y="554" width="16" height="16"/>
        <rect x="532" y="609" width="16" height="16"/>
      </g>
      <g class="viewfinder__stroke viewfinder__bracket">
        <path d="M525 434 H499 V486 H525"/>
        <path d="M555 434 H583 V486 H555"/>
      </g>
    </svg>

    <p class="cover__label">Sermon Serie</p>
  </main>
</body>
</html>
```